Business card design needed

I need a business card for my Sydney Painting Business, that specialises in painting High -end residential homes. i want the design to look clean, modern and edgy. i also want a logo next to the RK Decorating, using RKD together.

Industry/Entity Type

Residential

Contact Information for Business Card

RK Decorating (business name),LIC 581062B, Rob Kellaway, robert.kellaway@fernmail.net, mobile 0412573068

```html
<!DOCTYPE html>
<html lang="en">
<head>
<meta charset="utf-8">
<title>RK Decorating – Business Card</title>
<link rel="stylesheet" href="https://fonts.googleapis.com/css2?family=Cabin:wght@400;500&display=swap">
<style>
  :root {
    --page-bg: #eeeae4;
    --card-blue: #0aa7cc;
    --card-white: #ffffff;
    --accent-yellow: #e4e33a;
    --icon-yellow: #f2e21a;
    --text-white: #ffffff;
    --brand-blue: #17a3c4;
    --tile-blue: #1590bd;
    --tile-green: #5db64a;
    --tile-lime: #b8d433;
    --tile-gold: #f2bf1f;
    --tile-pink: #f0c6c4;
    --tile-sand: #e8d2b0;
    --shadow: rgba(0, 0, 0, 0.18);
  }
  * { margin: 0; padding: 0; box-sizing: border-box; }
  html, body { width: 1200px; height: 1000px; overflow: hidden; }
  body {
    background: var(--page-bg);
    font-family: "Cabin", "Gill Sans", sans-serif;
    position: relative;
  }
  .card {
    position: absolute;
    width: 780px;
    height: 446px;
    box-shadow: 0 6px 18px var(--shadow);
    overflow: hidden;
  }
  .card--front { left: 60px; top: 40px; background: var(--card-blue); }
  .card--back { left: 360px; top: 514px; background: var(--card-white); }

  .tile-band {
    position: absolute;
    top: 0;
    width: 150px;
    height: 100%;
    background: linear-gradient(180deg,
      var(--tile-gold) 0%, var(--tile-green) 12%, var(--tile-blue) 26%,
      var(--tile-lime) 38%, var(--tile-sand) 48%, var(--tile-pink) 58%,
      var(--tile-green) 66%, var(--tile-blue) 76%, var(--tile-lime) 88%,
      var(--tile-gold) 100%);
  }
  .card--front .tile-band { right: 0; }
  .card--back .tile-band { left: 0; }

  .front-brand {
    position: absolute;
    left: 44px;
    top: 62px;
    display: flex;
    align-items: baseline;
    gap: 18px;
    color: var(--text-white);
    font-weight: 400;
  }
  .brand-mark { font-size: 84px; line-height: 1; letter-spacing: 1px; }
  .brand-name { font-size: 34px; letter-spacing: 8px; }

  .header-rule {
    position: absolute;
    left: 0;
    top: 170px;
    width: 630px;
    height: 8px;
    background: var(--accent-yellow);
  }
  .person-name {
    position: absolute;
    left: 70px;
    top: 200px;
    font-size: 56px;
    font-weight: 500;
    color: var(--text-white);
  }
  .contact-list {
    position: absolute;
    left: 80px;
    top: 300px;
    list-style: none;
    color: var(--text-white);
    font-size: 24px;
  }
  .contact-list li { display: flex; align-items: center; gap: 24px; height: 40px; }
  .contact-icon { width: 36px; height: 28px; fill: var(--icon-yellow); flex: none; }

  .back-brand {
    position: absolute;
    left: 150px;
    right: 0;
    top: 120px;
    text-align: center;
    color: var(--brand-blue);
    font-weight: 400;
  }
  .back-brand .brand-mark { display: block; font-size: 100px; }
  .back-brand .brand-name { display: block; font-size: 38px; letter-spacing: 9px; margin-top: 6px; }
</style>
</head>
<body>
  <section class="card card--front">
    <div class="front-brand">
      <span class="brand-mark">RKD</span>
      <span class="brand-name">RK.DECORATING</span>
    </div>
    <div class="header-rule"></div>
    <h1 class="person-name">Rob Kellaway</h1>
    <ul class="contact-list">
      <li>
        <svg class="contact-icon" viewBox="0 0 36 28" aria-hidden="true">
          <polygon points="18,2 34,13 2,13"/>
          <rect x="6" y="13" width="24" height="13"/>
        </svg>
        LIC 581062B
      </li>
      <li>
        <svg class="contact-icon" viewBox="0 0 36 28" aria-hidden="true">
          <rect x="4" y="4" width="28" height="20"/>
          <polyline points="4,4 18,16 32,4" fill="none" stroke="#0aa7cc" stroke-width="2"/>
        </svg>
        robert.kellaway@fernmail.net
      </li>
      <li>
        <svg class="contact-icon" viewBox="0 0 36 28" aria-hidden="true">
          <path d="M3 10 Q18 0 33 10 L29 14 L24 11 L24 8 Q18 6 12 8 L12 11 L7 14 Z"/>
          <path d="M9 15 L27 15 L31 26 L5 26 Z"/>
          <circle cx="18" cy="20" r="3" fill="#0aa7cc"/>
        </svg>
        0412573068
      </li>
    </ul>
    <div class="tile-band" role="img" aria-label="Column of coloured triangle tiles in blue, green, lime, gold, pink and sand"></div>
  </section>

  <section class="card card--back">
    <div class="tile-band" role="img" aria-label="Column of coloured triangle tiles in blue, green, lime, gold, pink and sand"></div>
    <div class="back-brand">
      <span class="brand-mark">RKD</span>
      <span class="brand-name">RK.DECORATING</span>
    </div>
  </section>
</body>
</html>
```